Business Card Design for Marketing Firm

Looking for business card design for higher end marketing firm. Clean but impressionable/trendy. We are a marketing firm that represents manufacturers in the foodservice equipment and supply industry. Our customers are end users such has hotels, restaurants, country clubs, convention centers and casinos as well as distributors of restaurants supplies and equipment, and manufacturers of foodservice equipment and supplies.
Target Market(s)
Hotels, Restaurants, Supply & Equipment Distributors, Foodservice Manufacturers
Industry/Entity Type
Foodservice/Hospitality
Contact Information for Business Card
Name, Title, Contact Number, Email, Website, Social Media, Address
Requirements
Must have
- Clean & Simple but Serious and Impressionable

```html
<!DOCTYPE html>
<html lang="en">
<head>
<meta charset="utf-8">
<title>Harbor Table Reps – Business Card</title>
<link href="https://fonts.googleapis.com/css2?family=Cinzel:wght@400&family=Poppins:wght@400&display=swap" rel="stylesheet">
<style>
  :root {
    --backdrop: #1e1e20;
    --card-navy: #04037c;
    --card-navy-deep: #020163;
    --pattern-glow: #2a2ad8;
    --ink-white: #ffffff;
    --rule-soft: rgba(255,255,255,0.45);
  }
  * { box-sizing: border-box; margin: 0; padding: 0; }
  html, body { width: 1200px; height: 1108px; overflow: hidden; }
  body {
    background: var(--backdrop);
    display: flex;
    align-items: center;
    justify-content: center;
    gap: 80px;
  }
  .card {
    position: relative;
    width: 460px;
    height: 760px;
    border-radius: 28px;
    background: var(--card-navy);
    color: var(--ink-white);
    overflow: hidden;
  }
  .card-front {
    display: flex;
    flex-direction: column;
    align-items: center;
    padding-top: 150px;
  }
  .brand-name {
    font-family: "Poppins", sans-serif;
    font-weight: 400;
    font-size: 26px;
    letter-spacing: 1px;
    display: flex;
    align-items: center;
    gap: 12px;
    white-space: nowrap;
  }
  .brand-name .brand-dot {
    width: 14px; height: 14px; border-radius: 50%;
    background: var(--ink-white);
  }
  .person-name {
    margin-top: 110px;
    font-family: "Cinzel", serif;
    font-size: 33px;
    letter-spacing: 1px;
  }
  .person-title {
    font-family: "Poppins", sans-serif;
    font-size: 17px;
    letter-spacing: 1px;
  }
  .rule-row {
    display: flex;
    align-items: center;
    gap: 10px;
    width: 300px;
  }
  .rule-row .rule { flex: 1; height: 1px; background: var(--rule-soft); }
  .icon-row { margin-top: 28px; }
  .icon-box {
    width: 34px; height: 34px;
    background: var(--ink-white);
    border-radius: 6px;
    display: flex; align-items: center; justify-content: center;
  }
  .contact-list {
    margin-top: 14px;
    font-family: "Poppins", sans-serif;
    font-size: 19px;
    line-height: 1.5;
    text-align: center;
  }
  .address {
    margin-top: 14px;
    padding-top: 14px;
    border-top: 1px solid var(--rule-soft);
    width: 300px;
    font-family: "Poppins", sans-serif;
    font-size: 19px;
    line-height: 1.4;
    text-align: center;
  }
  .social-row { margin-top: 26px; }
  .social-circle {
    width: 32px; height: 32px;
    border: 1.5px solid var(--ink-white);
    border-radius: 50%;
  }
  .card-back .pattern-field {
    position: absolute; inset: 0;
    background:
      radial-gradient(ellipse at 80% 20%, var(--pattern-glow) 0%, transparent 45%),
      linear-gradient(160deg, var(--card-navy) 0%, var(--card-navy-deep) 100%);
  }
  .card-back .back-name {
    position: absolute;
    left: 0; right: 0;
    top: 560px;
    justify-content: center;
  }
</style>
</head>
<body>
  <section class="card card-front">
    <div class="brand-name"><span class="brand-dot"></span>Harbor Table Reps</div>
    <div class="person-name">DANIEL REYES</div>
    <div class="person-title">MANAGING DIRECTOR</div>

    <div class="rule-row icon-row">
      <span class="rule"></span>
      <span class="icon-box">
        <svg width="20" height="20" viewBox="0 0 24 24" aria-label="phone"><path fill="#04037c" d="M6.6 10.8a15 15 0 0 0 6.6 6.6l2.2-2.2c.3-.3.7-.4 1-.2 1.1.4 2.3.6 3.6.6.6 0 1 .4 1 1V20c0 .6-.4 1-1 1A17 17 0 0 1 3 4c0-.6.4-1 1-1h3.5c.6 0 1 .4 1 1 0 1.3.2 2.5.6 3.6.1.3 0 .7-.2 1z"/></svg>
      </span>
      <span class="icon-box">
        <svg width="20" height="20" viewBox="0 0 24 24" aria-label="email"><rect x="3" y="5" width="18" height="14" rx="1" fill="none" stroke="#04037c" stroke-width="2"/><path d="M3 6l9 7 9-7M3 19l7-6M21 19l-7-6" fill="none" stroke="#04037c" stroke-width="2"/></svg>
      </span>
      <span class="icon-box">
        <svg width="20" height="20" viewBox="0 0 24 24" aria-label="website"><circle cx="12" cy="12" r="9" fill="none" stroke="#04037c" stroke-width="2"/><ellipse cx="12" cy="12" rx="4" ry="9" fill="none" stroke="#04037c" stroke-width="1.6"/><path d="M3 12h18" stroke="#04037c" stroke-width="1.6"/></svg>
      </span>
      <span class="rule"></span>
    </div>

    <div class="contact-list">
      <p>044-987 654 321</p>
      <p>hello@harbortable.com</p>
      <p>www.harbortable.com</p>
    </div>

    <div class="address">
      <p>88 Quay Street, Suite 4</p>
      <p>30817, Portland</p>
    </div>

    <div class="rule-row social-row">
      <span class="rule"></span>
      <span class="social-circle"></span>
      <span class="social-circle"></span>
      <span class="social-circle"></span>
      <span class="rule"></span>
    </div>
  </section>

  <section class="card card-back">
    <div class="pattern-field" role="img" aria-label="Repeating tone-on-tone brand monogram pattern across the card"></div>
    <div class="brand-name back-name"><span class="brand-dot"></span>Harbor Table Reps</div>
  </section>
</body>
</html>
```